Ashworth Web Design Project

I need the front page and an internal page designed for this client's website. The logo is attached. Obviously the colors have to go with and/or work with the logo colors. I also attached a very rough brochure layout to help you see the direction we're going in with print materials. The rough site map is also attached. I see a slider on the homepage, the art for which I may come back to you to create. This clinic is in a very high end Dallas neighborhood. The hook is that it's a primary care and urgent facility with convenient hours.

I don't know how much this impacts your design, but this will be a Wordpress site and I'm using a framework called Struxo (struxo-demo.example). If Struxo proves to be inflexible, I'll have to get a template that allows me to execute your design.

This site (http://oakbendcareclinic.example) has the type and quality of content I will eventually have on the Ashworth site.

I just revised the brief for this project. I added the site map and added details to the overview and the "Must Have" section. Thank you for revisiting the brief. 

Reason: Christmas was a bad time to end it.

Target Market(s)

Women 25-54 with children living at home, income over $150k/year

Industry/Entity Type

Clinic

Requirements
Must have
• Masthead incorporating the logo
Followed by the primary nav
Slider on the home page below that
Dual nav - 1 with the nav in the attached site map
2 secondary nav with areas of healthcare
There will three blocks under the nav
1. It's about time (with a small blurb less than 50 words.
2. It's about choices (with small blurb)
3. It's about you (with small blurb)
Three footer blocks
patient check in link on every page
"No appointment? No problem" icon on every page

```html
<!DOCTYPE html>
<html lang="en">
<head>
<meta charset="utf-8">
<title>Ashworth Medical</title>
<link href="https://fonts.googleapis.com/css2?family=Arimo:ital,wght@0,400;0,700;1,700&display=swap" rel="stylesheet">
<style>
:root{
  --blue:#0b5ea8;
  --blue-dark:#064b8c;
  --green:#1aa94a;
  --green-light:#3fd46a;
  --text:#555;
  --grey-line:#ccc;
  --white:#fff;
}
*{box-sizing:border-box;margin:0;padding:0}
html,body{width:1017px;height:1200px;overflow:hidden;background:var(--white)}
body{position:relative;font-family:Arimo,Arial,sans-serif;color:var(--text);font-size:10px}
.abs{position:absolute}
.utility{left:735px;top:0;width:180px;height:22px;border:1px solid #ccc;border-top:0;border-radius:0 0 4px 4px;display:flex;gap:12px;justify-content:center;align-items:center;font-size:10.5px;font-weight:700;color:#555}
.utility span::before{content:"";display:inline-block;width:8px;height:8px;background:#777;margin-right:4px;border-radius:1px}
.social{left:842px;top:33px;display:flex;gap:7px}
.social i{width:20px;height:20px;background:var(--blue);border-radius:2px;display:block}
.brand{left:101px;top:42px;display:flex;align-items:center;gap:6px}
.brand-dot{width:40px;height:40px;border-radius:50%;background:var(--blue)}
.brand-name{font-size:26px;font-weight:700;color:var(--blue);letter-spacing:-.5px;line-height:30px}
.brand-tag{left:171px;top:77px;font-size:8.5px;font-weight:700;color:#444}
.mainnav{left:389px;top:60px;display:flex;gap:22px;align-items:center}
.mainnav a{font-size:12px;color:var(--green);text-decoration:none;padding:5px 0}
.mainnav a.current{background:var(--green);color:#fff;padding:5px 10px}
.slider{left:101px;top:95px;width:814px;height:294px;border-radius:8px;overflow:hidden;background:linear-gradient(120deg,#6b8a3a,#b8562d 50%,#7a9a4a)}
.slide-list{position:absolute;left:0;top:0;width:299px;height:294px;background:rgba(25,110,180,.85)}
.slide-item{position:absolute;left:18px;width:270px;height:76px}
.slide-item .thumb{position:absolute;left:0;top:0;width:97px;height:70px;background:#8a8a8a}
.slide-item h3{position:absolute;left:110px;top:0;font-size:10px;color:#fff;font-weight:700}
.slide-item p{position:absolute;left:110px;top:20px;width:160px;font-size:9.5px;color:#fff;line-height:11.5px}
.slide-item .more{position:absolute;left:177px;top:62px;font-size:9px;font-weight:700;color:#fff}
.slide-item.dim{opacity:.45}
.slide-rule{position:absolute;left:24px;width:255px;height:1px;background:rgba(255,255,255,.5)}
.checkin{left:101px;top:403px;width:814px;height:38px;border-radius:6px;background:linear-gradient(#5de27d,var(--green))}
.checkin i{position:absolute;left:276px;top:8px;width:18px;height:20px;border-radius:50%;background:#f0c040}
.checkin .field{position:absolute;left:305px;top:8px;width:205px;height:22px;background:#fff;border:1px solid #9ad;font-size:10px;color:#999;padding:5px 6px}
.checkin .btn{position:absolute;left:515px;top:7px;width:87px;height:24px;background:linear-gradient(#6be68a,#24b24f);border:1px solid #fff;color:#fff;font-weight:700;font-size:10px;text-align:center;line-height:22px}
.welcome{left:101px;top:463px;font-size:15px;color:var(--blue);font-weight:400}
.welcome b{font-weight:400;color:var(--green)}
.intro{left:103px;top:500px;width:552px;font-size:9.6px;line-height:11.5px}
.intro p{margin-bottom:11px}
.more-link{font-size:10px;font-weight:700;color:var(--blue)}
.feature{top:641px;width:180px;text-align:center}
.feature .icon{margin:0 auto;width:92px;height:92px;border-radius:50%;background:radial-gradient(circle at 50% 45%,#f4f4f4 38%,#1e5bb0 40%,#0a3f85 70%)}
.feature .shadow{margin:6px auto 0;width:70px;height:8px;border-radius:50%;background:#e4e4e4}
.feature h2{margin-top:16px;font-size:14.5px;font-weight:400;color:var(--green)}
.feature h2 span{color:var(--blue)}
.feature p{margin-top:10px;font-size:9.6px;line-height:11.4px}
.feature .btn{margin:16px auto 0;width:110px;height:29px;border-radius:15px;border:1px solid #999;background:linear-gradient(#fff,#ddd);color:#333;font-size:11.5px;line-height:27px}
.carenav{left:675px;top:463px;width:240px;border-top:1px dotted #888}
.carenav li{list-style:none;height:23px;border-bottom:1px dotted #888;background:linear-gradient(#fff,#eaeaea);font-size:10px;color:#555;line-height:22px;padding-left:25px;position:relative}
.carenav li::before{content:"";position:absolute;left:9px;top:7px;border-left:7px solid #555;border-top:4px solid transparent;border-bottom:4px solid transparent}
.carenav li.active{background:var(--blue);color:#fff}
.carenav li.active::before{border-left-color:#fff}
.noappt{left:675px;top:641px;width:240px;height:67px;border-radius:5px;background:var(--blue)}
.noappt h4{position:absolute;left:7px;top:14px;font-size:11px;color:#fff}
.noappt .btn{position:absolute;left:46px;top:40px;width:72px;height:18px;background:var(--green);color:#fff;font-size:8px;font-weight:700;text-align:center;line-height:18px;border:1px solid #8e8}
.noappt .badge{position:absolute;left:180px;top:8px;width:50px;height:50px;border-radius:6px;background:linear-gradient(135deg,#e8e8e8,#c9c9c9 55%,#7bc87a)}
.bloghead{left:675px;top:731px;width:240px;height:30px;background:var(--green);color:#fff}
.bloghead h3{position:absolute;left:7px;top:7px;font-size:13px}
.bloghead span{position:absolute;right:8px;top:10px;font-size:9.5px}
.post{left:682px;width:230px;font-size:9.6px;line-height:11.4px}
.post h5{font-size:10px;color:var(--blue);margin-bottom:12px}
.post h5 em{color:#666;font-weight:400}
.post .more-link{font-size:10px;font-weight:400}
.post-rule{left:682px;top:855px;width:225px;border-top:1px dotted #999}
.footer{left:101px;top:968px;width:814px;height:232px;border-radius:8px 8px 0 0;background:var(--blue);color:#fff}
.fcol{position:absolute;top:30px}
.fcol h4{font-size:12px;margin-bottom:8px}
.fcol li{list-style:none;font-size:9.8px;line-height:17.7px}
.fcol li i{display:inline-block;width:9px;height:9px;background:#dfe8f5;margin-right:6px;vertical-align:-1px}
.fsep{position:absolute;top:30px;width:1px;height:125px;background:rgba(255,255,255,.35)}
.ffield{position:absolute;left:560px;width:214px;height:22px;background:var(--blue-dark);border:1px solid #5b9be0;font-style:italic;font-weight:700;font-size:10px;padding:4px 7px}
.fsend{position:absolute;left:688px;top:164px;width:86px;height:22px;background:linear-gradient(#6be68a,#1aa94a);border:1px solid #fff;font-weight:700;text-align:center;line-height:20px}
.fbottom{position:absolute;top:201px;font-size:9.8px}
.fbottom .lbl{color:#ff9a30}
</style>
</head>
<body>
<div class="abs utility"><span>Login</span><span>Register</span><span>Blog</span></div>
<div class="abs social"><i></i><i></i><i></i></div>
<div class="abs brand"><div class="brand-dot"></div><div class="brand-name">AshworthMedical</div></div>
<div class="abs brand-tag">Immediate Family and Personal Care</div>
<nav class="abs mainnav"><a class="current">HOME</a><a>ABOUT</a><a>SERVICES</a><a>STAFF</a><a>INSURANCE</a><a>VIDEO</a><a>CONTACT US</a></nav>

<section class="abs slider" role="img" aria-label="Photo of a mother and two children lying on the grass with lollipops">
  <div class="slide-list">
    <div class="slide-item dim" style="top:15px"><div class="thumb" role="img" aria-label="Mother holding baby photo"></div><h3>LOREM IPSUM DOLOR SIT AMET</h3><p>Lorem ipsum dolor sit amet, conse ctetur adipiscing elit. Cras iaculis n ulla non tellus molestie rhoncus.</p><div class="more">FIND OUT MORE ▸▸</div></div>
    <div class="slide-rule" style="top:100px"></div>
    <div class="slide-item" style="top:115px"><div class="thumb" style="background:#7b8f4a" role="img" aria-label="Family lying on grass photo"></div><h3>LOREM IPSUM DOLOR SIT AMET</h3><p>Lorem ipsum dolor sit amet, conse ctetur adipiscing elit. Cras iaculis n ulla non tellus molestie rhoncus.</p><div class="more">FIND OUT MORE ▸▸</div></div>
    <div class="slide-rule" style="top:197px"></div>
    <div class="slide-item dim" style="top:210px"><div class="thumb" role="img" aria-label="Spa stone treatment photo"></div><h3>LOREM IPSUM DOLOR SIT AMET</h3><p>Lorem ipsum dolor sit amet, conse ctetur adipiscing elit. Cras iaculis n ulla non tellus molestie rhoncus.</p><div class="more">FIND OUT MORE ▸▸</div></div>
  </div>
</section>

<div class="abs checkin"><i></i><div class="field">Patient Check In</div><div class="btn">CHECK IN</div></div>

<h1 class="abs welcome">Welcome to Ashworth <b>Medical</b></h1>
<div class="abs intro">
  <p>Lorem ipsum dolor sit amet, consectetur adipiscing elit. Cras iaculis nulla non tellus molestie rhoncus. Maecenas blandit aliqu am dolor eget fringilla. Integer egestas dignissim iaculis. Nulla a nibh erat, eu hendrerit erat. Morbi tristique erat et neque lacini a porta. Vestibulum fringilla, felis vel cursus ultrices.</p>
  <p>Magna arcu accumsan nulla, vel euismod lorem est at nibh. Vivamus ac augue ac sapien eleifend tempus. Fusce vel nulla neq ue. Etiam at ante sed ligula aliquam placerat. Curabitur porta pulvinar quam, nec interdum eros fermentum vitae. Lorem ipsum dolor sit amet, consectetur adipiscing elit. Cras iaculis nulla non tellus molestie rhoncus. Maecenas blandit aliquam dolor eget fringilla.</p>
  <p class="more-link">FIND OUT MORE ▸▸</p>
</div>

<div class="abs feature" style="left:95px"><div class="icon" role="img" aria-label="Clock icon"></div><div class="shadow"></div><h2><span>It's</span> about time</h2><p>Lorem ipsum dolor sit amet, consectet adipiscing elit. Cras commodo, enim eget ornare convallis, felis orci congue massa, in volutpat magna neque ultrici massa. Vivamus ac mauris elit, non pr risus. Sed cursus, felis nec vehicula auctor, nibh mauris eleifend nisl, a dict um orci turpis sit amet lorem.</p><div class="btn">Keep Reading</div></div>
<div class="abs feature" style="left:282px"><div class="icon" role="img" aria-label="Arrows icon"></div><div class="shadow"></div><h2><span>It's</span> about choices</h2><p>Lorem ipsum dolor sit amet, consectet adipiscing elit. Cras commodo, enim eget ornare convallis, felis orci congue massa, in volutpat magna neque ultrici massa. Vivamus ac mauris elit, non pr risus. Sed cursus, felis nec vehicula auctor, nibh mauris eleifend nisl, a dict um orci turpis sit amet lorem.</p><div class="btn">Keep Reading</div></div>
<div class="abs feature" style="left:478px"><div class="icon" role="img" aria-label="Person icon"></div><div class="shadow"></div><h2><span>It's</span> about you</h2><p>Lorem ipsum dolor sit amet, consectet adipiscing elit. Cras commodo, enim eget ornare convallis, felis orci congue massa, in volutpat magna neque ultrici massa. Vivamus ac mauris elit, non pr risus. Sed cursus, felis nec vehicula auctor, nibh mauris eleifend nisl, a dict um orci turpis sit amet lorem.</p><div class="btn">Keep Reading</div></div>

<ul class="abs carenav">
  <li class="active">Immediate Care</li><li>Allergies</li><li>Primary Care</li><li>Women's Health</li><li>Medical Spa Treatments</li><li>Men's Health</li><li>Weight Loss</li>
</ul>

<div class="abs noappt"><h4>"No appointment? No problem"</h4><div class="btn">LEARN MORE</div>
<div class="badge" role="img" aria-label="Walk-in care illustration: crossed-out clock with medical plus"></div></div>

<div class="abs bloghead"><h3>From Our Blog</h3><span>view blog archieve</span></div>
<div class="abs post" style="top:774px"><h5>The Title of the post <em>25-12-12</em></h5><p>Lorem ipsum dolor sit amet, consectetur adipiscing elit. Cras commodo, enim eget ornare convallis, felis orci congue massa, in volutpat magna neque ultricies massa. <span class="more-link">FIND OUT MORE ▸▸</span></p></div>
<div class="abs post-rule"></div>
<div class="abs post" style="top:863px"><h5>The Title of the post <em>25-12-12</em></h5><p>Lorem ipsum dolor sit amet, consectetur adipiscing elit. Cras commodo, enim eget ornare convallis, felis orci congue massa, in volutpat magna neque ultricies massa. <span class="more-link">FIND OUT MORE ▸▸</span></p></div>

<footer class="abs footer">
  <div class="fcol" style="left:40px"><h4>Lorem ipsum dolor</h4><ul><li>Vivamus ac mauris elit</li><li>Morbi a nibh quis</li><li>Phasellus dictum</li><li>Suspendisse libero</li><li>Proin eu ante sed</li><li>Vestibulum sagittis velit</li></ul></div>
  <div class="fsep" style="left:176px"></div>
  <div class="fcol" style="left:213px"><h4>Lorem ipsum dolor</h4><ul><li>Vivamus ac mauris elit</li><li>Morbi a nibh quis</li><li>Phasellus dictum</li><li>Suspendisse libero</li><li>Proin eu ante sed</li><li>Vestibulum sagittis velit</li></ul></div>
  <div class="fsep" style="left:352px"></div>
  <div class="fcol" style="left:393px"><h4>Follow us on</h4><ul><li><i></i>Friendbook</li><li><i></i>Chirper</li><li><i></i>ClipTube</li></ul></div>
  <div class="fsep" style="left:502px"></div>
  <div class="fcol" style="left:563px"><h4>Contact us</h4></div>
  <div class="ffield" style="top:54px">Name</div>
  <div class="ffield" style="top:81px">Email</div>
  <div class="ffield" style="top:108px;height:47px">Your Comments</div>
  <div class="fsend">SEND</div>
  <div class="fbottom" style="left:42px"><span class="lbl">Tel:</span> +1-555-0142-870 &nbsp;| &nbsp;<span class="lbl">email:</span> info@ashworthmedical.example</div>
  <div class="fbottom" style="right:40px">Copyright © 2012-2013 Ashworth Medical</div>
</footer>
</body>
</html>
```